依頼詳細
ネット企業のため、「シンプル」で「オシャレ」なデザインを希望します。横でも縦でもかまいません。ロゴデータを添付しますので、ロゴを生かしたデザインでお願いいたします。名刺の背景は白地となります。
記載項目
●表面

ロゴ:別途添付
会社名:株式会社tenrift(←小文字アルファベット)
役職:架空
氏名:架空(漢字プラス小さめの文字でローマ字表記)
郵便番号:架空
住所:架空
電話:架空
メールアドレス:架空

●裏面

WEB集客に関する事ならお任せ下さい。(←少し大きめで)

事業内容
SEO・SEMコンサルティング
WEBマーケティング
WEB広告事業

著書
月収820万円!画面で稼ぐ5つの法則(出版:嶺光ブックス)
http://q3vtrdn.example/maru/zt41
希望イメージ
シンプル 複雑
単色 カラフル
暗い 明るい
日常 高級
遊び心 厳粛
未来的 伝統的
女性的 男性的
希望する色
納品ファイル
• 高解像度JPG (.jpg)
• イラストレーター形式 (.ai)
• フォトショップ形式 (.psd)
補足説明
※補足説明
決定後、架空の部分を実際の物への変更をお願いします。
■ 選んだ理由

弊社ロゴを活用し、うまくまとめていただきました。

■ 提案者全員のお礼・コメント

たくさんのご提案をいただきまして、ありがとうございました。
またよろしくお願いいたします。

```html
<!DOCTYPE html>
<html lang="ja">
<head>
<meta charset="utf-8">
<title>tenrift 名刺デザイン</title>
<link rel="stylesheet" href="https://fonts.googleapis.com/css2?family=Noto+Sans+JP:wght@400;500;700&display=swap">
<style>
  :root {
    --brand-blue: #2a8fd8;
    --brand-blue-light: #5aaee6;
    --accent-gray: #4a4d52;
    --ink: #333538;
    --ink-soft: #55585c;
    --card-bg: #ffffff;
    --page-bg: #ffffff;
    --card-edge: #d9dbde;
  }
  * { box-sizing: border-box; margin: 0; padding: 0; }
  html, body { width: 805px; height: 1200px; overflow: hidden; background: var(--page-bg); }
  body { position: relative; font-family: "Noto Sans JP", sans-serif; color: var(--ink); }

  .swatch { position: absolute; width: 58px; height: 58px; }
  .swatch--blue { background: var(--brand-blue); }
  .swatch--light { background: var(--brand-blue-light); }
  .swatch--gray { background: var(--accent-gray); }

  .card {
    position: absolute; left: 21px; width: 778px; height: 496px;
    background: var(--card-bg); border: 1px solid var(--card-edge);
    box-shadow: 0 2px 6px rgba(0,0,0,0.12);
  }
  .card--front { top: 107px; }
  .card--back { top: 702px; }

  .brand { position: absolute; left: 40px; width: 240px; text-align: center; }
  .brand__mark { display: block; width: 96px; height: 96px; margin: 0 auto 14px; background: var(--brand-blue); }
  .brand__name { font-size: 54px; font-weight: 700; color: var(--brand-blue); line-height: 1; letter-spacing: -1px; }
  .card--front .brand { top: 235px; }
  .card--back .brand { top: 215px; }

  .details { position: absolute; left: 352px; top: 160px; }
  .details__role { font-size: 16px; color: var(--ink); }
  .details__name { margin-top: 6px; font-size: 34px; font-weight: 500; letter-spacing: 6px; }
  .details__roman { font-size: 14px; letter-spacing: 0; margin-left: 18px; color: var(--ink-soft); }
  .details__company { margin-top: 14px; font-size: 21px; font-weight: 700; color: var(--brand-blue); }
  .details__contact { margin-top: 6px; font-size: 14px; line-height: 1.55; color: var(--ink); }

  .pitch { position: absolute; left: 352px; top: 230px; }
  .pitch__lead { font-size: 26px; font-weight: 500; color: var(--brand-blue); }
  .pitch__heading { margin-top: 18px; font-size: 15px; font-weight: 700; color: var(--brand-blue); }
  .pitch__heading + .pitch__list { margin-top: 2px; }
  .pitch__list { list-style: none; font-size: 14px; line-height: 1.5; color: var(--brand-blue); }
  .pitch__heading--book { margin-top: 10px; }
</style>
</head>
<body>
  <div class="swatch swatch--blue" style="left:10px; top:0;"></div>
  <div class="swatch swatch--light" style="left:80px; top:0;"></div>
  <div class="swatch swatch--gray" style="left:155px; top:0;"></div>

  <section class="card card--front" aria-label="名刺 表面">
    <div class="brand">
      <span class="brand__mark"></span>
      <div class="brand__name">tenrift</div>
    </div>
    <div class="details">
      <p class="details__role">代表取締役</p>
      <p class="details__name">川野 誠<span class="details__roman">makoto kawano</span></p>
      <p class="details__company">株式会社 tenrift</p>
      <p class="details__contact">
        〒105-0014 東京都港区芝浜2-8-6<br>
        tel.03-5821-4470 fax.03-5821-4471<br>
        mobile.090-7316-2258<br>
        kawano@tenrift.co.jp<br>
        http://www.tenrift.co.jp
      </p>
    </div>
  </section>

  <div class="swatch swatch--blue" style="left:0; top:612px;"></div>
  <div class="swatch swatch--light" style="left:0; top:670px; height:26px;"></div>

  <section class="card card--back" aria-label="名刺 裏面">
    <div class="brand">
      <span class="brand__mark"></span>
      <div class="brand__name">tenrift</div>
    </div>
    <div class="pitch">
      <p class="pitch__lead">WEB集客に関する事ならお任せ下さい。</p>
      <p class="pitch__heading">事業内容:</p>
      <ul class="pitch__list">
        <li>SEO・SEMコンサルティング</li>
        <li>WEBマーケティング</li>
        <li>WEB広告事業</li>
      </ul>
      <p class="pitch__heading pitch__heading--book">著 書</p>
      <ul class="pitch__list">
        <li>月収820万円!画面で稼ぐ5つの法則(出版:嶺光ブックス)</li>
        <li>http://q3vtrdn.example/maru/zt41</li>
      </ul>
    </div>
  </section>
</body>
</html>
```